Coastal Rubdown Oil Co. needs a new label.

This massage oil has been in Australia for over 20 years and needs a new label for its plastic 250ml bottles. The current label (8cm x 8cm) looks old fashioned and so we are looking for something that reflects freedom, relaxation, inspiration. The product is made from sweet almond oil and has different essential oils used to give unique smells. I have seen some lovely abstract vector images. I think we need a clean straight look with bright colours. There are currently six variations to the product. "Weary and Worn Heads, Achy and Spent Frames, Couples Mix, Heather Soak Oil, Unwinding Mix, Uplift Mix" Different coloured labels have been used for each of the blends. I have included photos of existing bottles plus some ideas for the labels.

I would like to use the same font on the name of the brand Bramblewick Acres. If we change the font it may be difficult for existing customers to find our product.

Also just under the name Bramblewick Acres I would like to insert a type of logo (can be the shape of a tear drop or round circle) to say:

Massage Oil
Since 1970

The size of the label is 8cm x 12 cm for the front and the same size for the back of the label.
Updates

Coastal Rubdown oil Company has posted on the brief some images from Pixelvault plus two photos of the original bottles. I am looking for a new design which is bright in colour, fun and funky. I am not thinking along the lines of the traditional Herb and trees look. I think the original label is too busy and the colours overpower the label. The other point I think that is important is that the product has been around since 1970. If there is room I think a round logo which says: Massage Oil Since 1970 I am hoping that we can fit this information on the label Looking forward to seeing all the designs come thru. So far I have only had two designs come thru. Speak soon from hot sunny Australia. maree

Thank you to everyone who has already posted designs for our Massage Label. I have now edited the brief to include some more ideas on how to make this design the Best! I will email back to you straight away ideas and thoughts on your designs. Remember I live in Australia and can be either 10hrs in front or behind your time.

Reason: Due to busy lives and commitments over the next few days I feel that an extension will benefit all involved. Thank you to everyone who has submitted designs and working with me to create something beautiful. maree

Hello from Australia all the designers who have submitted some wonderful designs over the past two weeks. We are now entering the final three days of the competition. Thank you to everyone who has worked so hard to try and create the perfect label for my massage oil bottle. All of you have done a fantastic job. This has made the decision hard to make. Thank you to everyone. Please submit all your last minute designs soon. kind regards maree Australia

Target Market(s)

The type of person purchasing a massage oil blend will buy from a health food shop, pharmacy or from an on-line store. I believe they are wanting something bright that clearly communicates that that it is a massage oil.

Industry/Entity Type

Massage

Font styles to use
Script

Requirements
Must have
• Different colour for each massage oil blend.
Need same font for the name Bramblewick Acres. (script font or similar)

Abstract design please.
Nice to have
• A logo under the name Bramblewick Acres

Tear Drop or circle design that says:

Massage Oil
Since 1970

also we would like an outline for the back label. (see photo attached)

BACK LABEL information

A unique blend of essential oils in a fine light base.

Contains:

vegetable oil extract of nettle, sweet almond oil, ethanol, essential oils of lavender, lemongrass, orange & ylang ylang and vitamin E.

How to Use:

Shake well warm bottle in warm water if very cold.
Lovingly massage the body from head to toe.
Not for medicinal use.

Bramblewick Acres
Hollin WA 6099
Phone: (08) 9555 0142

(LEAVE ROOM FOR BARCODE)
Should not have
• Too busy design or old fashioned design.
No dull colours.

```html
<!DOCTYPE html>
<html lang="en">
<head>
<meta charset="utf-8">
<title>Bramblewick Acres – Massage Oil Labels</title>
<link rel="stylesheet" href="https://fonts.googleapis.com/css2?family=Pinyon+Script&family=Marcellus&family=Crimson+Text:wght@700&display=swap">
<style>
  :root {
    --page: #ffffff;
    --gold-dark: #7a3f10;
    --gold-mid: #c9782a;
    --gold-light: #f0b45a;
    --band-text: #fff6e4;
    --marker: #f07a16;

    --uplift-deep: #f2b431;
    --uplift-light: #fde7a3;
    --uplift-ink: #3a2614;
    --uplift-size: #6a3a0c;

    --weary-deep: #41cfe2;
    --weary-light: #d2f6fa;
    --weary-ink: #1b2a8c;
    --weary-size: #1a237e;

    --heather-deep: #a879dc;
    --heather-light: #f1e6fb;
    --heather-ink: #3a1f78;
    --heather-size: #5a2490;
  }
  * { box-sizing: border-box; margin: 0; padding: 0; }
  html, body { width: 1200px; height: 824px; overflow: hidden; background: var(--page); }
  .canvas { position: relative; width: 1200px; height: 824px; overflow: hidden; }

  .label {
    position: absolute;
    width: 370px;
    height: 550px;
    box-shadow: 0 6px 14px rgba(0,0,0,0.18);
    overflow: hidden;
    font-family: "Marcellus", serif;
  }
  .label--uplift {
    left: 25px; top: 175px; transform: rotate(-6deg);
    background: linear-gradient(160deg, var(--uplift-light) 0%, var(--uplift-deep) 55%, var(--uplift-light) 100%);
    --ink: var(--uplift-ink); --size-ink: var(--uplift-size);
  }
  .label--weary {
    left: 393px; top: 123px; transform: rotate(-1.5deg);
    background: linear-gradient(160deg, var(--weary-light) 0%, var(--weary-deep) 55%, var(--weary-light) 100%);
    --ink: var(--weary-ink); --size-ink: var(--weary-size);
  }
  .label--heather {
    left: 677px; top: 190px; transform: rotate(6deg);
    background: linear-gradient(160deg, var(--heather-light) 0%, var(--heather-deep) 60%, var(--heather-light) 100%);
    --ink: var(--heather-ink); --size-ink: var(--heather-size);
  }

  .maker {
    position: absolute; left: 0; right: 0; top: 30px;
    display: flex; align-items: center; justify-content: center; gap: 7px;
    font-size: 13px; color: var(--ink); white-space: nowrap;
  }
  .maker__dot { width: 12px; height: 12px; border-radius: 50%; background: var(--marker); }

  .brand {
    position: absolute; left: 0; right: 0; top: 88px;
    font-family: "Pinyon Script", cursive; font-weight: 400;
    color: var(--ink);
    font-size: 54px; line-height: 1;
  }
  .brand__first { display: block; padding-left: 28px; }
  .brand__second { display: block; padding-left: 150px; }

  .blend-band {
    position: absolute; left: 47px; width: 276px; top: 295px; height: 96px;
    border-radius: 8px;
    background: linear-gradient(180deg, var(--gold-light) 0%, var(--gold-mid) 45%, var(--gold-dark) 100%);
    box-shadow: 0 2px 4px rgba(0,0,0,0.25);
    display: flex; flex-direction: column; align-items: center; justify-content: center;
    color: var(--band-text); text-align: center; text-transform: uppercase;
  }
  .blend-band__kind { font-size: 18px; letter-spacing: 0.5px; line-height: 1.1; }
  .blend-band__name { font-size: 28px; line-height: 1.05; }
  .blend-band__sub { font-size: 15px; letter-spacing: 1px; line-height: 1.2; }

  .bloom {
    position: absolute; left: 85px; top: 395px; width: 200px; height: 120px;
    border-radius: 50%;
    background: radial-gradient(ellipse at center, rgba(255,255,255,0.85) 0%, rgba(255,255,255,0.4) 45%, rgba(255,255,255,0) 72%);
  }

  .volume {
    position: absolute; left: 0; right: 0; top: 508px; text-align: center;
    font-family: "Crimson Text", serif; font-weight: 700;
    font-size: 20px; color: var(--size-ink);
  }
</style>
</head>
<body>
<main class="canvas">

  <section class="label label--uplift">
    <p class="maker"><span class="maker__dot"></span>Coastal Rubdown Oil Co.</p>
    <h1 class="brand"><span class="brand__first">Bramblewick</span><span class="brand__second">Acres</span></h1>
    <div class="blend-band">
      <span class="blend-band__kind">Massage Oil</span>
      <span class="blend-band__name">Uplift</span>
      <span class="blend-band__sub">Mix</span>
    </div>
    <div class="bloom" role="img" aria-label="Soft abstract blossom illustration in golden tones"></div>
    <p class="volume">250ml</p>
  </section>

  <section class="label label--weary">
    <p class="maker"><span class="maker__dot"></span>Coastal Rubdown Oil Co.</p>
    <h2 class="brand"><span class="brand__first">Bramblewick</span><span class="brand__second">Acres</span></h2>
    <div class="blend-band">
      <span class="blend-band__kind">Massage Oil</span>
      <span class="blend-band__name">Weary &amp;</span>
      <span class="blend-band__sub">Worn Heads</span>
    </div>
    <div class="bloom" role="img" aria-label="Soft abstract blossom illustration in aqua tones"></div>
    <p class="volume">250ml</p>
  </section>

  <section class="label label--heather">
    <p class="maker"><span class="maker__dot"></span>Coastal Rubdown Oil Co.</p>
    <h2 class="brand"><span class="brand__first">Bramblewick</span><span class="brand__second">Acres</span></h2>
    <div class="blend-band">
      <span class="blend-band__kind">Massage Oil</span>
      <span class="blend-band__name">Heather</span>
      <span class="blend-band__sub">Soak Oil</span>
    </div>
    <div class="bloom" role="img" aria-label="Soft abstract blossom illustration in lilac tones"></div>
    <p class="volume">250ml</p>
  </section>

</main>
</body>
</html>
```